Kestrel Roofing & Restoration Business Card Design

Lookiing for a double sided business card design that will have rounded corners, will look good with Spot UV, Soft Laminate, or Gloss
Front of card should have Logo, Name and Contact Info, License numbers
Back of card should have Logo, maybe other small details

```html
<!DOCTYPE html>
<html lang="en">
<head>
<meta charset="utf-8">
<title>Kestrel Roofing &amp; Restoration – Business Card</title>
<link rel="stylesheet" href="https://fonts.googleapis.com/css2?family=Montserrat:wght@700&family=Arimo:wght@400;700&display=swap">
<style>
  :root {
    --page: #e8e8e7;
    --card: #202021;
    --card-deep: #1a1a1b;
    --accent: #1596d6;
    --edge: #0d86c4;
    --ink: #f2f2f2;
    --muted: #d9d9d9;
    --rule: #bdbdbd;
  }
  * { box-sizing: border-box; margin: 0; padding: 0; }
  html, body { width: 1200px; height: 801px; overflow: hidden; }
  body {
    background: var(--page);
    display: flex;
    align-items: center;
    justify-content: center;
    gap: 48px;
  }
  .card {
    position: relative;
    width: 536px;
    height: 306px;
    background: linear-gradient(135deg, var(--card) 0%, var(--card-deep) 100%);
    border-bottom: 4px solid var(--edge);
    box-shadow: 0 14px 28px rgba(0,0,0,.22);
    overflow: hidden;
  }

  /* Front */
  .brand {
    position: absolute;
    left: 38px;
    top: 50%;
    transform: translateY(-50%);
    display: flex;
    align-items: center;
    gap: 10px;
  }
  .brand__mark {
    width: 12px; height: 12px;
    background: var(--accent);
  }
  .brand__name {
    font-family: "Montserrat", sans-serif;
    font-weight: 700;
    color: var(--ink);
    font-size: 15px;
    line-height: 1.25;
    letter-spacing: .04em;
    text-transform: uppercase;
  }
  .divider {
    position: absolute;
    left: 262px;
    top: 52px;
    bottom: 52px;
    width: 1px;
    background: var(--rule);
  }
  .contact {
    position: absolute;
    left: 282px;
    top: 52px;
    font-family: "Arimo", sans-serif;
    color: var(--muted);
    font-size: 13.5px;
    line-height: 1.3;
  }
  .contact__name {
    color: var(--accent);
    font-weight: 700;
    font-size: 18px;
    letter-spacing: .02em;
    text-transform: uppercase;
  }
  .contact__title { margin-bottom: 10px; }
  .contact__address { margin-bottom: 10px; }
  .contact__line {
    display: flex;
    align-items: center;
    gap: 7px;
  }
  .contact__icon { width: 12px; height: 12px; flex: none; fill: var(--accent); }

  /* Back */
  .back__brand {
    position: absolute;
    left: 70px;
    top: 50%;
    transform: translateY(-50%);
    display: flex;
    align-items: center;
    gap: 18px;
  }
  .back__mark {
    width: 16px; height: 16px;
    background: var(--accent);
  }
  .back__name {
    font-family: "Montserrat", sans-serif;
    font-weight: 700;
    color: var(--ink);
    font-size: 30px;
    line-height: 1.2;
    letter-spacing: .04em;
    text-transform: uppercase;
  }
</style>
</head>
<body>

  <section class="card card--front" aria-label="Front of business card">
    <div class="brand">
      <span class="brand__mark"></span>
      <p class="brand__name">Kestrel<br>Roofing &amp;<br>Restoration</p>
    </div>
    <span class="divider"></span>
    <div class="contact">
      <p class="contact__name">Marcus Hale</p>
      <p class="contact__title">Managing Director</p>
      <p class="contact__address">Your Address, City<br>State, Zip 0000</p>
      <p class="contact__line">
        <svg class="contact__icon" viewBox="0 0 24 24" aria-hidden="true"><path d="M6.6 10.8a15 15 0 0 0 6.6 6.6l2.2-2.2c.3-.3.7-.4 1-.2 1.1.4 2.3.6 3.6.6.6 0 1 .4 1 1V20c0 .6-.4 1-1 1A17 17 0 0 1 3 4c0-.6.4-1 1-1h3.5c.6 0 1 .4 1 1 0 1.3.2 2.5.6 3.6.1.3 0 .7-.2 1z"/></svg>
        044-555 218 704
      </p>
      <p class="contact__line">
        <svg class="contact__icon" viewBox="0 0 24 24" aria-hidden="true"><path d="M2 5h20v14H2zm2 2v.5l8 5 8-5V7z"/></svg>
        info@kestrelroof.com
      </p>
      <p class="contact__line">
        <svg class="contact__icon" viewBox="0 0 24 24" aria-hidden="true"><circle cx="12" cy="12" r="10"/></svg>
        www.kestrelroof.com
      </p>
    </div>
  </section>

  <section class="card card--back" aria-label="Back of business card">
    <div class="back__brand">
      <span class="back__mark"></span>
      <p class="back__name">Kestrel<br>Roofing &amp;<br>Restoration</p>
    </div>
  </section>

</body>
</html>
```